Cigarette Packaging for a luxury smoking brand

I need to do a new packaging for my cigarette brand new flavor and i need you to provide me with the source files and also with renders with 3d mockups. The design must include the cigarette box for 20 cigs, the outer box that contains 10 package of 20 cigs each, and the cigarrette must also be designed using black paper. I will provide our logo and other information that's required. The new flavor is called "Orvo". You can see our other product designs at www.torvel.uk but the layout you can freely change it as long the design contains the name "TORVEL" and the logo symbol, and the flavor name "Orvo"
Updates

Dear Designers. Thank you very much for your work.
Sadly i was unaware that the www.torvel.uk website was attacked by a malware and that the page was offline. I apologize for that. The issue is solved now and the page is back on. I like some of the designs seen, but sadly the designs are too focused on the logo and not on the stylish or luxury concept. I suggest you have a look on how we use the logo on the existing designs on torvel.uk and find a way to make a unique design based on your creativity. Please feel free to message me if you have any question or suggestion and i will be happy to assist. Focus more on the name and flavor and a smaller logo somewhere in the package and not big logo.

Target Market(s)

Tobacco consumers

Industry/Entity Type

tobacco

Colors

Designer to choose only greyscale colors for use in the design.

Requirements
Must have
• My name and logo, name can be any color but logo is usually on debossed or embossed with gold foil
Nice to have
• i would prefer a dark or black packaging
Should not have
• pink nor girly colors,

```html
<!DOCTYPE html>
<html lang="en">
<head>
<meta charset="utf-8">
<title>TORVEL Orvo – Pack Dieline</title>
<link rel="stylesheet" href="https://fonts.googleapis.com/css2?family=Cinzel:wght@500&family=Libre+Baskerville&family=Great+Vibes&display=swap">
<style>
  :root {
    --paper: #ffffff;
    --board: #000000;
    --gold: #c9a24a;
    --gold-light: #ead9a0;
    --gold-deep: #8f6a22;
    --ink-light: #e8e4da;
  }
  html, body {
    margin: 0;
    padding: 0;
    width: 1200px;
    height: 1200px;
    overflow: hidden;
    background: var(--paper);
  }
  .dieline {
    display: block;
    width: 1200px;
    height: 1200px;
  }
  .panel { fill: var(--board); }
  .rope-band { fill: url(#ropeTone); }
  .texture-area { fill: url(#stripeTone); }
  .flavour-frame {
    fill: none;
    stroke: var(--gold);
    stroke-width: 1.2;
  }
  .brand-name {
    font-family: "Cinzel", serif;
    font-weight: 500;
    font-size: 40px;
    letter-spacing: 2px;
    fill: var(--gold);
  }
  .product-line {
    font-family: "Libre Baskerville", serif;
    font-size: 8.5px;
    letter-spacing: 0.8px;
    fill: var(--ink-light);
  }
  .flavour-name {
    font-family: "Great Vibes", cursive;
    font-size: 17px;
    fill: var(--gold);
  }
  .pack-count {
    font-family: "Libre Baskerville", serif;
    font-size: 8.5px;
    letter-spacing: 0.6px;
    fill: var(--ink-light);
  }
  .crest-area { fill: url(#crestGlow); }
</style>
</head>
<body>
<svg class="dieline" viewBox="0 0 1932 1932" xmlns="http://www.w3.org/2000/svg">
  <defs>
    <linearGradient id="ropeTone" x1="0" y1="0" x2="1" y2="0">
      <stop offset="0" stop-color="#a98535"/>
      <stop offset="0.5" stop-color="#d9bd72"/>
      <stop offset="1" stop-color="#a98535"/>
    </linearGradient>
    <linearGradient id="stripeTone" x1="0" y1="0" x2="0" y2="1">
      <stop offset="0" stop-color="#000000"/>
      <stop offset="1" stop-color="#2a2210"/>
    </linearGradient>
    <radialGradient id="crestGlow" cx="0.5" cy="0.5" r="0.5">
      <stop offset="0" stop-color="#e3c577"/>
      <stop offset="0.7" stop-color="#b48a35"/>
      <stop offset="1" stop-color="#b48a35" stop-opacity="0"/>
    </radialGradient>
  </defs>

  <!-- front face with top flaps -->
  <path class="panel" d="M661 279 L787 353 L1054 353 L1180 279 L1180 704 L661 704 Z"/>

  <rect class="texture-area" x="661" y="455" width="519" height="249" role="img" aria-label="Fine vertical gold stripe texture"/>

  <rect class="rope-band" x="661" y="684" width="519" height="6" role="img" aria-label="Twisted gold rope band"/>

  <text class="brand-name" x="920" y="395" text-anchor="middle">TORVEL</text>
  <text class="product-line" x="920" y="413" text-anchor="middle">FILTER CIGARETTES</text>

  <!-- flavour frame -->
  <path class="flavour-frame" d="M893 456 L853 456 Q849 456 849 460 L849 709 Q849 713 853 713 L987 713 Q991 713 991 709 L991 460 Q991 456 987 456 L948 456"/>
  <rect class="panel" x="893" y="446" width="55" height="18"/>
  <text class="flavour-name" x="920" y="462" text-anchor="middle">Orvo</text>
  <text class="pack-count" x="920" y="658" text-anchor="middle">KING SIZE</text>
  <text class="pack-count" x="918" y="670" text-anchor="middle">20 CLASS A CIGARETTES</text>

  <!-- top tuck, back face and bottom tuck -->
  <path class="panel" d="
    M661 725 L762 725 Q770 705 792 705 L1050 705 Q1072 705 1078 725 L1178 725 Q1199 725 1199 747
    L1199 812 Q1199 832 1179 834 L1179 1195 L1103 1251 L1119 1255 L1159 1237 L1177 1252 L1177 1333
    Q1199 1340 1199 1360 L1199 1420 Q1199 1444 1176 1444 L1078 1444 Q1072 1462 1050 1465 L790 1465
    Q768 1462 762 1444 L662 1444 Q641 1444 641 1422 L641 1360 Q641 1336 665 1335 L665 1253 L683 1238
    L724 1255 L738 1251 L662 1195 L662 834 Q641 830 641 808 L641 747 Q641 725 661 725 Z"/>

  <rect class="rope-band" x="661" y="850" width="518" height="6" role="img" aria-label="Twisted gold rope band"/>

  <!-- bottom face with dust flap -->
  <path class="panel" d="M661 1474 L1179 1474 L1179 1540 L1054 1615 L1054 1747 L787 1747 L787 1615 L661 1540 Z"/>
  <rect class="rope-band" x="661" y="1479" width="518" height="6" role="img" aria-label="Twisted gold rope band"/>
  <ellipse class="crest-area" cx="920" cy="1560" rx="58" ry="36" role="img" aria-label="Gold foil brand crest area"/>
</svg>
</body>
</html>
```